36" inch (height) x 96" inch (width) Banner for Baseball Field

Hello. This project is an advertisement that will be printed onto a 3 foot by 8 foot full color banner and placed at little league fields in Southern California. A theme of the banner can be baseball. The company is my law office practicing Estate Planning and Tax Law. I am uploading the current business card, which has the logo, website, and telephone number. You can also pull images from www.rkpembrove.com I would like the banner to be a fun design that incorporates baseball somehow, but draws attention to my law and tax office, and my website. Please be creative, and have fun with it. The colors of my practice are included in the logo. At the bottom, it should say "Attorney Advertisement," but this can be in very small font in the bottom right or left corner.

Target Market(s)

Youth Baseball Fans

Industry/Entity Type

Law; Accounting

Colors

Designer to choose colors to be used in the design.

Requirements
Must have
• My telephone number. My website.
Nice to have
• Would like to see "Estate Planning" and "Tax Law and Preparation" Would also like to see "Attorney" and "CPA" or "Certified Public Accountant" prominently diplayed

```html
<!DOCTYPE html>
<html lang="en">
<head>
<meta charset="utf-8">
<title>RK Pembrove Ballfield Banner</title>
<link rel="stylesheet" href="https://fonts.googleapis.com/css2?family=Cinzel:wght@400;500&family=Montserrat:wght@500;700;800&family=Open+Sans:wght@400&display=swap">
<style>
  :root {
    --backdrop: #dedede;
    --night-top: #0d1f6e;
    --night-mid: #1f45b8;
    --stands: #141a2e;
    --field: #2f7a2a;
    --ink: #000000;
    --white: #ffffff;
    --navy-line: #1b2a78;
    --bar-green: #22e51a;
    --bar-green-dark: #16a812;
    --tag-blue: #2b93d6;
    --tag-text: #0b1d3a;
    --silver: #d9dde2;
  }
  * { margin: 0; padding: 0; box-sizing: border-box; }
  html, body { width: 1200px; height: 621px; overflow: hidden; background: var(--backdrop); }
  .canvas { position: relative; width: 1200px; height: 621px; }
  .banner {
    position: absolute; left: 64px; top: 107px; width: 1071px; height: 402px; overflow: hidden;
    background: linear-gradient(180deg, var(--night-top) 0%, var(--night-mid) 28%, var(--stands) 55%, var(--field) 78%, #000 88%);
  }
  .banner > * { position: absolute; }
  .art { position: absolute; }
  .website {
    left: 0; width: 100%; top: 40px; text-align: center;
    font-family: "Open Sans", sans-serif; font-size: 28px; color: var(--white); letter-spacing: 0.2px;
  }
  .website svg { vertical-align: -4px; margin-right: 6px; }
  .name-panel {
    left: 262px; top: 119px; width: 340px; height: 152px; background: var(--ink);
    border-top: 2px solid var(--white); border-bottom: 2px solid var(--white);
  }
  .brand { left: 300px; top: 128px; width: 246px; text-align: center; color: var(--white); }
  .brand-mark { width: 62px; height: 62px; border: 3px solid var(--white); border-radius: 50%; margin: 0 auto 8px; }
  .brand-kicker { font-family: "Cinzel", serif; font-size: 12px; letter-spacing: 0.6px; line-height: 1; }
  .brand-of { font-family: "Cinzel", serif; font-size: 7px; margin: 2px 0 1px; display: flex; align-items: center; gap: 5px; justify-content: center; }
  .brand-of::before, .brand-of::after { content: ""; width: 48px; height: 1px; background: var(--white); }
  .brand-name { font-family: "Cinzel", serif; font-size: 30px; line-height: 1.05; white-space: nowrap; margin-left: -30px; margin-right: -30px; }
  .service {
    background: var(--ink); color: var(--white); border: 2px solid var(--white); border-left: none;
    border-radius: 0 10px 10px 0; font-family: "Montserrat", sans-serif; font-weight: 700;
    font-size: 21px; line-height: 1; padding: 0 14px; display: flex; align-items: center; white-space: nowrap;
  }
  .service--estate { left: 597px; top: 131px; width: 208px; height: 31px; justify-content: flex-end; }
  .service--tax { left: 593px; top: 165px; width: 305px; height: 31px; justify-content: flex-end; }
  .service--attorney { left: 583px; top: 198px; width: 112px; height: 29px; justify-content: flex-end; }
  .service--cpa { left: 560px; top: 228px; width: 397px; height: 33px; font-size: 21px; justify-content: flex-end; }
  .address {
    left: 350px; top: 291px; width: 400px; text-align: center; color: var(--white);
    font-family: "Montserrat", sans-serif; font-weight: 500; font-size: 16px; line-height: 19px;
  }
  .address-pin { left: 352px; top: 294px; }
  .phone {
    left: 322px; top: 328px; color: var(--white); font-family: "Montserrat", sans-serif;
    font-weight: 800; font-size: 42px; line-height: 1; letter-spacing: 1px; display: flex; align-items: center; gap: 6px;
  }
  .cpa-word {
    left: 792px; top: 252px; font-family: "Montserrat", sans-serif; font-weight: 800; font-size: 92px;
    color: var(--silver); line-height: 1; letter-spacing: -3px;
  }
  .ad-tag {
    left: 850px; top: 355px; width: 175px; height: 22px; background: var(--tag-blue); color: var(--tag-text);
    font-family: "Montserrat", sans-serif; font-weight: 500; font-size: 12.5px; display: flex; align-items: center; justify-content: center;
  }
</style>
</head>
<body>
<div class="canvas">
  <div class="banner">
    <!-- stadium backdrop, ellipse player photo, glove and ball, portrait -->
    <svg class="art" width="1071" height="402" viewBox="0 0 1071 402">
      <defs>
        <linearGradient id="bars" x1="0" x2="1"><stop offset="0" stop-color="var(--bar-green)"/><stop offset="1" stop-color="var(--bar-green-dark)"/></linearGradient>
        <radialGradient id="player" cx="0.5" cy="0.45" r="0.6"><stop offset="0" stop-color="#b88a6e"/><stop offset="0.6" stop-color="#8a4a3c"/><stop offset="1" stop-color="#5a5a66"/></radialGradient>
        <linearGradient id="glove" x1="0" y1="0" x2="1" y2="1"><stop offset="0" stop-color="#d9824a"/><stop offset="1" stop-color="#8c4420"/></linearGradient>
        <linearGradient id="suit" x1="0" y1="0" x2="0" y2="1"><stop offset="0" stop-color="#7a5140"/><stop offset="0.5" stop-color="#d9a98a"/><stop offset="1" stop-color="#1d2230"/></linearGradient>
      </defs>
      <rect role="img" aria-label="Night baseball stadium with floodlights, stands and green infield" x="0" y="0" width="1071" height="402" fill="transparent"/>
      <g transform="translate(169 191) rotate(-40)">
        <ellipse rx="132" ry="104" fill="var(--white)"/>
        <ellipse rx="127" ry="99" fill="var(--navy-line)"/>
        <ellipse role="img" aria-label="Photo of a batter in a red jersey swinging a bat" rx="123" ry="95" fill="url(#player)"/>
      </g>
      <path role="img" aria-label="Photo of a leather baseball glove holding a ball" d="M0 225 Q80 215 140 300 Q175 350 165 402 L0 402 Z" fill="url(#glove)"/>
      <rect role="img" aria-label="Portrait photo of the attorney in a dark suit" x="816" y="9" width="145" height="187" rx="40" fill="url(#suit)"/>
      <g>
        <rect x="770" y="282" width="28" height="35" fill="url(#bars)"/>
        <rect x="891" y="200" width="39" height="128" fill="url(#bars)"/>
        <rect x="930" y="147" width="40" height="184" fill="url(#bars)"/>
        <rect x="970" y="82" width="56" height="251" fill="url(#bars)"/>
      </g>
    </svg>

    <div class="website">
      <svg width="22" height="22" viewBox="0 0 22 22" fill="none" stroke="#fff" stroke-width="1.6"><circle cx="11" cy="11" r="9.5"/><ellipse cx="11" cy="11" rx="4.5" ry="9.5"/><path d="M1.5 11h19M3 6h16M3 16h16"/></svg>www.rkpembrove.com
    </div>

    <div class="name-panel"></div>
    <div class="brand">
      <div class="brand-mark"></div>
      <div class="brand-kicker">THE LAW OFFICES</div>
      <div class="brand-of">OF</div>
      <div class="brand-name">RK PEMBROVE</div>
    </div>

    <div class="service service--estate">Estate Planning</div>
    <div class="service service--tax">Tax Law and Preparation</div>
    <div class="service service--attorney">Attorney</div>
    <div class="service service--cpa">Certified Public Accountant</div>

    <div class="cpa-word">CPA</div>

    <svg class="address-pin" width="28" height="32" viewBox="0 0 28 32" fill="none" stroke="#fff" stroke-width="2"><path d="M14 24 C8 16 6 13 6 9 a8 8 0 0 1 16 0 c0 4-2 7-8 15z"/><circle cx="14" cy="9" r="3"/><path d="M8 22 L2 30 H26 L20 22"/></svg>
    <div class="address">728 Alder Street Penthouse Suite 212<br>Maple Ridge, California 91399</div>

    <div class="phone">
      <svg width="44" height="44" viewBox="0 0 44 44" fill="none" stroke="#fff" stroke-width="2.4"><circle cx="22" cy="22" r="20"/><path d="M15 12c2-1 3 0 4 3l1 3c0 1-2 2-2 3 1 3 3 5 6 6 1 0 2-2 3-2l3 1c3 1 4 2 3 4-1 3-4 4-7 3-7-2-12-7-14-14-1-3 1-6 3-7z"/><path d="M26 13a6 6 0 0 1 5 5M27 9a10 10 0 0 1 8 8"/></svg>
      (805) 555-0142
    </div>

    <div class="ad-tag">Attorney Advertisement</div>
  </div>
</div>
</body>
</html>
```